Marlow Landscaping Landing Page

I require a landing page for my landscaping business.

My business plan revolves around hooking clients with weeding services. Not lawn herbicide sprays, but actual hand weeding and bed maintenance. I've found my niche as most people do not want to do this kind of work. From there I often upsell clients into actual hardscaping or softscaping.

I like things to be clean, concise, and to the point. Not overly flashy, but not so minimal that that it's boring. My logo is a very good example of what I like.

The business is LGBTQ owned and operated. I do not broadcast this but I feel the logo itself, along with the name is usually enough to tip people into assumption. I'm not opposed to color, but I do not want the page to scream "gay". My favourite color is yellow...

I used to be a door to door salesman so I'm doing something different where I want to do all my selling in my first meeting with the client. With this said I do not need a section for "work pictures", as I have photos of my work on my tablet, which I show the client during the consultation.

Ideally i'd like my web site to actually be just a landing page. I'd like room for all the following information within the page;

- description of services;
Weeding of Perennial and Flower Beds
Selective Pruning of Trees and Shrubs
Hedging
Landscape Construction
Landscape Design
Total Lawn Treatment Plans
Landscape Pest Control

- contact information, phone, email
Gerald Hanswick
204-731-4426
ger.hanswick@brelvanyard.com

- "free estimates" somewhere on the page that is either led to by the eye, or very easy to notice and see

- and my slogan which is "dependable, reliable, consistent"

- room for a link to my future ratewell account so they can see reviews from real people

- My Logo present

Any or all of these can be custom made graphics or simply text, whatever looks best

I do not want people to have to search for information throughout. Design it in such a way that either the eye flows naturally from one piece of information to the other, or that it's all compartmentalized neatly enough that everything is easy to find.

As I am a landscape and outdoor maintenance service I'm no opposed to images such as flowers, trees, landscaping, etc being present. However please note that my main focus and source of income comes from weeding services, everything else is bonus cash.

Many of my clients are extremely wealthy individuals who pay over $1000 for the season for me just to show up and pull weeds. So making the website appeal to wealthy people as opposed to the average joe is paramount.

I do not cut grass. Please do not have any indication on the website, either through writing or graphics that implies that I cut grass. There are enough companies doing that.

Target Market(s)

Wealthy, often elderly individuals.

Industry/Entity Type

Landscape Gardening

Coding

Coded - Design and coding required

Number of Pages Required

1 page

Font styles to use
Sans Serif

Colors

Designer to choose colors to be used in the design.

Requirements
Must have
• - description of services;
• Weeding of Perennial and Flower Beds
• Selective Pruning of Trees and Shrubs
• Hedging
• Landscape Construction
• Landscape Design
• Total Lawn Treatment Plans
• Landscape Pest Control
• - contact information, phone, email
• Gerald Hanswick
• 204-731-4426
• ger.hanswick@brelvanyard.com
• - "free estimates" somewhere on the page that is either led to by the eye, or very easy to notice and see
• - and my slogan which is "dependable, reliable, consistent"
• - room for a link to my future ratewell account so they can see reviews from real people
• - My Logo present
Nice to have
• Flowers or weeds depicted. Possibly some hardscaping and softscaping if it doesnt look too bulky and crowded.
Should not have
• grass

```html
<!DOCTYPE html>
<html lang="en">
<head>
<meta charset="utf-8">
<title>Marlow Landscaping</title>
<link rel="stylesheet" href="https://fonts.googleapis.com/css2?family=Roboto:wght@300;400;500;700;900&display=swap">
<style>
:root{
  --green:#1c9a4c;
  --green-dark:#107a3a;
  --yellow:#f6e71c;
  --ink:#1d1d1d;
  --grey:#555;
  --grey-light:#e9e9e9;
  --white:#fff;
  --footer:#262626;
}
*{box-sizing:border-box;margin:0;padding:0}
html,body{width:1200px;height:4235px;overflow:hidden}
body{position:relative;font-family:'Roboto',sans-serif;color:var(--ink);background:var(--white)}
.abs{position:absolute}
.photo{position:absolute}
.body-copy{font-size:16px;line-height:1.6;font-weight:400}
.btn{display:inline-block;padding:9px 22px;border:1px solid #bbb;border-radius:4px;background:var(--white);color:var(--ink);font-size:13px;font-weight:700;letter-spacing:.5px;text-decoration:none}
.spaced{letter-spacing:14px;font-weight:300;text-transform:uppercase}

/* hero */
.hero{position:absolute;left:0;top:0;width:1200px;height:580px;background:var(--white);overflow:hidden}
.hero-photo{left:0;top:0;width:1200px;height:580px;background:linear-gradient(160deg,#7c9b4a 0%,#3f6a2f 45%,#b86a72 80%,#d9557a 100%);clip-path:polygon(525px 0,1200px 0,1200px 580px,400px 580px)}
.hero-edge{left:0;top:0;width:1200px;height:580px;background:var(--yellow);clip-path:polygon(510px 0,525px 0,400px 580px,385px 580px)}
.logo{left:85px;top:120px;display:flex;align-items:center;gap:14px;font-size:50px;font-weight:500;color:var(--ink);letter-spacing:-.5px}
.logo-dot{width:30px;height:30px;border-radius:50%;background:var(--yellow)}
.slogan{left:85px;top:270px;font-size:52px;line-height:48px;text-transform:uppercase}
.slogan .strong{font-weight:900}
.slogan .light{font-weight:300}
.estimates{left:85px;top:448px;width:305px;height:76px;border-radius:8px;background:var(--green);color:var(--white);text-align:center;padding-top:10px}
.estimates .free{font-size:15px;letter-spacing:6px;font-weight:400}
.estimates .big{font-size:28px;font-weight:700;letter-spacing:1px}
.hero-prop{left:370px;top:470px;width:170px;height:95px;background:linear-gradient(#ece15a,#8a8a3a);border-radius:6px}
.social{right:0;top:70px;display:flex;flex-direction:column;gap:4px}
.social span{display:block;width:44px;height:44px}
.social .s1{background:#3b5998}.social .s2{background:#29a9e0}.social .s3{background:#c8232c}

/* contact */
.contact{position:absolute;left:0;top:580px;width:1200px;height:197px;background:var(--green);overflow:hidden}
.contact-yellow{left:0;top:0;width:1200px;height:197px;background:var(--yellow);clip-path:polygon(0 0,520px 0,440px 197px,0 197px)}
.contact-title{left:100px;top:60px;line-height:1}
.contact-title .big{font-size:56px;font-weight:900}
.contact-title .sub{font-size:30px;font-weight:300;letter-spacing:1px}
.contact-name{left:645px;top:28px;font-size:38px;font-weight:500;color:var(--white);letter-spacing:1px;text-transform:uppercase}
.contact-lines{left:525px;top:98px;display:flex;gap:30px;align-items:center;color:var(--white)}
.contact-lines div{display:flex;align-items:center;gap:12px}
.contact-lines .phone{font-size:40px;font-weight:500}
.contact-lines .mail{font-size:22px;font-weight:400}

/* services heading */
.services-head{position:absolute;left:0;top:777px;width:1200px;height:230px;background:var(--white)}
.silhouette{position:absolute;background:linear-gradient(#d4d4d4,#ececec)}
.services-head .kicker{position:absolute;left:0;width:1200px;top:72px;text-align:center;font-size:34px;font-weight:300;color:var(--grey);letter-spacing:1px}
.services-head h1{position:absolute;left:0;width:1200px;top:105px;text-align:center;font-size:72px;font-weight:700;color:#333}

/* weeding */
.pruning-band{position:absolute;left:0;top:1378px;width:1200px;height:500px;background:var(--green-dark)}
.weeding-card{position:absolute;left:85px;top:997px;width:1030px;height:463px;background:#f3f3f3;box-shadow:0 6px 22px rgba(0,0,0,.25);overflow:hidden}
.weeding-photo{right:0;top:0;width:420px;height:463px;background:linear-gradient(170deg,#c7303a 0%,#7a9a4a 40%,#9a9a88 100%);border-left:5px solid var(--yellow);border-radius:60% 0 0 0/100% 0 0 0}
.weeding-card h2{position:absolute;left:90px;top:60px;font-size:60px;font-weight:700;color:var(--green);line-height:1}
.weeding-card .sub{position:absolute;left:90px;top:128px;font-size:29px;font-weight:400;color:#333}
.weeding-card .body-copy{position:absolute;left:90px;top:198px;width:480px;color:var(--grey)}
.weeding-card .btn{position:absolute;left:90px;top:352px}

/* pruning */
.pruning-photo{left:0;top:1400px;width:375px;height:478px;background:linear-gradient(160deg,#4e7a38,#1f4a25);border:6px solid var(--yellow);border-left:none;border-radius:0 240px 240px 0}
.pruning-text{left:437px;top:1520px;width:680px;color:var(--white)}
.pruning-text .kicker{font-size:25px;font-weight:400}
.pruning-text h2{font-size:46px;font-weight:700;line-height:1.05;margin-bottom:14px}
.pruning-text .btn{margin-top:34px;border-color:var(--white)}

/* hedging */
.hedging{position:absolute;left:0;top:1878px;width:1200px;height:474px;background:var(--yellow);overflow:hidden}
.hedging-edge{left:0;top:0;width:1200px;height:474px;background:var(--green);clip-path:polygon(700px 0,725px 0,830px 237px,725px 474px,700px 474px,805px 237px)}
.hedging-photo{left:0;top:0;width:1200px;height:474px;background:linear-gradient(135deg,#8a6a3a,#5a7a3a 50%,#a04a2a);clip-path:polygon(725px 0,1200px 0,1200px 474px,725px 474px,830px 237px)}
.hedging h2{position:absolute;left:85px;top:68px;font-size:66px;font-weight:700;color:#2b2b2b}
.hedging .body-copy{position:absolute;left:85px;top:170px;width:600px;color:#333}
.hedging .btn{position:absolute;left:85px;top:355px}

/* construction */
.construction{position:absolute;left:0;top:2352px;width:1200px;height:599px;background:var(--white)}
.construction-photo{left:0;top:0;width:485px;height:599px;background:linear-gradient(170deg,#6f8a3a,#a59a7a 45%,#6a7a5a 75%,#e0c84a)}
.construction-head{left:285px;top:55px;border-left:8px solid var(--yellow);background:var(--white);padding:10px 30px 10px 48px;box-shadow:14px 16px 18px -14px rgba(0,0,0,.3)}
.construction-head .spaced{font-size:50px;line-height:1;color:#333}
.construction-head h2{font-size:54px;font-weight:700;color:var(--green);line-height:1.1}
.construction .body-copy{position:absolute;left:525px;top:260px;width:590px;color:#333}
.construction .btn{position:absolute;left:525px;top:520px}

/* design */
.design{position:absolute;left:0;top:2951px;width:1200px;height:494px;background:var(--green);overflow:hidden}
.design-photo{left:0;top:0;width:1200px;height:494px;background:linear-gradient(160deg,#9ab85a,#3f7a35 60%,#2f5a28);clip-path:polygon(800px 0,1200px 0,1200px 494px,680px 494px)}
.design .body-copy{position:absolute;left:85px;top:60px;width:430px;color:var(--white)}
.design .body-copy p+p{margin-top:16px}
.design .btn{position:absolute;left:85px;top:392px;border-color:var(--white)}
.design-box{left:530px;top:215px;width:320px;height:210px;background:var(--yellow);box-shadow:0 6px 18px rgba(0,0,0,.3);display:flex;flex-direction:column;align-items:center;justify-content:center}
.design-box .spaced{font-size:27px;letter-spacing:9px;color:var(--green-dark);margin-right:-9px}
.design-box h2{font-size:58px;font-weight:700;color:var(--green-dark);line-height:1}

/* lawn */
.lawn{position:absolute;left:0;top:3445px;width:1200px;height:390px;text-align:center}
.lawn .spaced{position:absolute;left:0;width:1200px;top:75px;font-size:32px;color:#333}
.lawn h2{position:absolute;left:0;width:1200px;top:112px;font-size:58px;font-weight:700;color:var(--green)}
.lawn .body-copy{position:absolute;left:180px;top:205px;width:840px;color:#333}
.lawn .btn{position:absolute;left:525px;top:300px}

/* pest */
.pest{position:absolute;left:0;top:3835px;width:1200px;height:339px;background:var(--yellow);overflow:hidden}
.pest-photo{left:0;top:0;width:460px;height:339px;background:linear-gradient(135deg,#5a8a3a,#d6d6c0 55%,#3a6a2a);clip-path:polygon(0 0,350px 0,440px 170px,350px 339px,0 339px)}
.pest .spaced{position:absolute;left:525px;top:45px;font-size:40px;color:#333}
.pest h2{position:absolute;left:525px;top:92px;font-size:44px;font-weight:700;color:var(--green)}
.pest .body-copy{position:absolute;left:525px;top:160px;width:590px;color:#333}
.pest .btn{position:absolute;left:525px;top:258px}

.footer{position:absolute;left:0;top:4174px;width:1200px;height:61px;background:var(--footer);color:#999;font-size:12px;text-align:center;line-height:61px}
</style>
</head>
<body>

<header class="hero">
  <div class="photo hero-photo" role="img" aria-label="Photo of a garden path lined with trees and flowering shrubs"></div>
  <div class="abs hero-edge"></div>
  <div class="abs logo"><span>MARLOW LANDSCAPING</span><span class="logo-dot"></span></div>
  <div class="abs slogan"><div class="strong">Dependable,</div><div class="light">Reliable,</div><div class="light">Consistent</div></div>
  <a class="abs estimates" href="#contact"><div class="free">FREE</div><div class="big">ESTIMATES</div></a>
  <div class="abs hero-prop" role="img" aria-label="Illustration of garden equipment"></div>
  <div class="abs social"><span class="s1"></span><span class="s2"></span><span class="s3"></span></div>
</header>

<section class="contact" id="contact">
  <div class="abs contact-yellow"></div>
  <div class="abs contact-title"><div class="big">CONTACT</div><div class="sub">INFORMATION</div></div>
  <div class="abs contact-name">Gerald Hanswick</div>
  <div class="abs contact-lines">
    <div><svg width="34" height="34" viewBox="0 0 24 24"><path fill="#fff" d="M6.6 10.8a15 15 0 0 0 6.6 6.6l2.2-2.2c.3-.3.7-.4 1-.2 1.1.4 2.3.6 3.6.6.6 0 1 .4 1 1V20c0 .6-.4 1-1 1A17 17 0 0 1 3 4c0-.6.4-1 1-1h3.5c.6 0 1 .4 1 1 0 1.3.2 2.5.6 3.6.1.3 0 .7-.2 1z"/></svg><span class="phone">204-731-4426</span></div>
    <div><svg width="34" height="26" viewBox="0 0 24 18"><path fill="#fff" d="M0 0h24v2L12 9 0 2z M0 4l12 7 12-7v14H0z"/></svg><span class="mail">ger.hanswick@brelvanyard.com</span></div>
  </div>
</section>

<section class="services-head">
  <div class="silhouette" style="left:40px;top:30px;width:130px;height:200px" role="img" aria-label="Silhouette of a gardener at work"></div>
  <div class="silhouette" style="left:395px;top:90px;width:90px;height:120px" role="img" aria-label="Silhouette of a gardener kneeling"></div>
  <div class="silhouette" style="left:820px;top:90px;width:90px;height:130px" role="img" aria-label="Silhouette of a gardener tending plants"></div>
  <div class="silhouette" style="left:1070px;top:20px;width:130px;height:210px" role="img" aria-label="Silhouette of a gardener watering"></div>
  <div class="kicker">DESCRIPTION OF</div>
  <h1>SERVICES</h1>
</section>

<div class="pruning-band"></div>

<article class="weeding-card">
  <div class="photo weeding-photo" role="img" aria-label="Photo of a tidy flower bed with red blooms and stones"></div>
  <h2>WEEDING OF</h2>
  <div class="sub">PERENNIAL AND FLOWER BEDS</div>
  <p class="body-copy">Lorem ipsum dolor sit amet, consectetur adipiscing elit. Sed sit amet ultrices massa. Duis sed diam non dui faucibus consequat. Aenean placerat neque ipsum, eget luctus sem auctor nec. Donec placerat ultrices enim sed finibus. Vestibulum sapien leo, fermentum vitae metus ut, rhoncus bibendum metus.</p>
  <a class="btn" href="#contact">READ MORE</a>
</article>

<div class="photo pruning-photo" role="img" aria-label="Photo of neatly pruned shrubs"></div>
<article class="abs pruning-text">
  <div class="kicker">SELECTIVE PRUNING OF</div>
  <h2>TREES AND SHRUBS</h2>
  <p class="body-copy">Lorem ipsum dolor sit amet, consectetur adipiscing elit. Sed sit amet ultrices massa. Duis sed diam non dui faucibus consequat. Aenean placerat neque ipsum, eget luctus sem auctor nec. Donec placerat ultrices enim sed finibus. Vestibulum sapien leo, fermentum vitae metus ut, rhoncus bibendum metus.</p>
  <a class="btn" href="#contact">READ MORE</a>
</article>

<section class="hedging">
  <div class="abs hedging-edge"></div>
  <div class="photo hedging-photo" role="img" aria-label="Photo of hands trimming a hedge with shears"></div>
  <h2>HEDGING</h2>
  <p class="body-copy">Lorem ipsum dolor sit amet, consectetur adipiscing elit. Sed sit amet ultrices massa. Duis sed diam non dui faucibus consequat. Aenean placerat neque ipsum, eget luctus sem auctor nec. Donec placerat ultrices enim sed finibus. Vestibulum sapien leo, fermentum vitae metus ut, rhoncus bibendum metus. Sed sit amet ultrices massa. Duis sed diam non dui faucibus consequat. Aenean placerat neque ipsum, eget luctus sem auctor nec.</p>
  <a class="btn" href="#contact">READ MORE</a>
</section>

<section class="construction">
  <div class="photo construction-photo" role="img" aria-label="Photo of a stone-edged pond with benches and yellow flowers"></div>
  <div class="abs construction-head"><div class="spaced">Landscape</div><h2>CONSTRUCTION</h2></div>
  <p class="body-copy">Lorem ipsum dolor sit amet, consectetur adipiscing elit. Sed sit amet ultrices massa. Duis sed diam non dui faucibus consequat. Aenean placerat neque ipsum, eget luctus sem auctor nec. Donec placerat ultrices enim sed finibus. Vestibulum sapien leo, fermentum vitae metus ut, rhoncus bibendum metus. Sed sit amet ultrices massa. Duis sed diam non dui faucibus consequat. Aenean placerat neque ipsum, eget luctus sem auctor nec. Donec placerat ultrices enim sed finibus. Vestibulum sapien leo, fermentum vitae metus ut, rhoncus bibendum metus Sed sit amet ultrices massa. Duis sed diam non dui faucibus consequat.</p>
  <a class="btn" href="#contact">READ MORE</a>
</section>

<section class="design">
  <div class="photo design-photo" role="img" aria-label="Photo of a designed garden with trees and ferns"></div>
  <div class="body-copy">
    <p>Lorem ipsum dolor sit amet, consectetur adipiscing elit. Sed sit amet ultrices massa. Duis sed diam non dui faucibus consequat. Aenean placerat neque ipsum, eget luctus sem auctor nec. Donec placerat ultrices enim sed finibus. Vestibulum sapien leo, fermentum vitae metus ut, rhoncus bibendum metus.</p>
    <p>Duis sed diam non dui faucibus consequat. Aenean placerat neque ipsum, eget luctus sem auctor nec. Donec placerat ultrices enim sed finibus. Vestibulum sapien leo, fermentum vitae metus ut, rhoncus bibendum metus.</p>
  </div>
  <a class="btn" href="#contact">READ MORE</a>
  <div class="abs design-box"><div class="spaced">Landscape</div><h2>DESIGN</h2></div>
</section>

<section class="lawn">
  <div class="spaced">Total Lawn</div>
  <h2>TREATMENT PLANS</h2>
  <p class="body-copy">Lorem ipsum dolor sit amet, consectetur adipiscing elit. Sed sit amet ultrices massa. Duis sed diam non dui faucibus consequat. Aenean placerat neque ipsum, eget luctus sem auctor nec. Donec placerat ultrices enim sed finibus. Vestibulum sapien leo, fermentum vitae metus ut, rhoncus bibendum metus.</p>
  <a class="btn" href="#contact">READ MORE</a>
</section>

<section class="pest">
  <div class="photo pest-photo" role="img" aria-label="Photo of a spray bottle treating white flowers"></div>
  <div class="spaced">Landscape</div>
  <h2>PEST CONTROL</h2>
  <p class="body-copy">Lorem ipsum dolor sit amet, consectetur adipiscing elit. Sed sit amet ultrices massa. Duis sed diam non dui faucibus consequat. Aenean placerat neque ipsum, eget luctus sem auctor nec.</p>
  <a class="btn" href="#contact">READ MORE</a>
</section>

<footer class="footer">© 2017 Marlow Landscaping. All Rights Reserved.</footer>

</body>
</html>
```